Halvorsen Construction Needs a Business Card

Our current business card is very bland, and since we have a new logo, we would like a new business card design to reflect our company. It can be a single-sided or two-sided card, but it is important that our contact information appears on the same side. I am attaching a copy of our old card and our new logo. If you need the logo in another format than the one I'm sending, please let me know. This is the information that we must have on our card, but not necessarily in any specific order:
1) Our logo
2) General Contractor
3) Dale Halvorsen, Owner
4) 482 Commerce Ridge Road, Brookfield Bend, Vermont 35871
5) Office: 555-555-0147
7) Fax: 555-555-0148
8) Cell: 555-555-0193
9) halvorsenconstruction@qvl-mail.net
10) halvorsenconstruction-example.com (can be omitted if necessary)
Also, I will need files in a format that I can alter if any of the above information changes in the near future. Thank you in advance for your submissions!
Target Market(s)
Commercial and residential clients, architects, and subcontractors.
Industry/Entity Type
Business
Look and feel

```html
<!DOCTYPE html>
<html lang="en">
<head>
<meta charset="utf-8">
<title>Halvorsen Construction – Business Card</title>
<link rel="stylesheet" href="https://fonts.googleapis.com/css2?family=Open+Sans:wght@400;800&display=swap">
<style>
  :root {
    --backdrop: #3b3b3b;
    --card-white: #ffffff;
    --safety-yellow: #fbc413;
    --swoosh-light: #f6d978;
    --ink: #1e1e1e;
    --panel-dark: #2a2a2a;
    --grime: #3a2c2c;
    --text-light: #ffffff;
  }
  * { box-sizing: border-box; margin: 0; padding: 0; }
  html, body {
    width: 1200px; height: 750px; overflow: hidden;
    background: var(--backdrop);
    font-family: "Open Sans", Arial, sans-serif;
  }
  .card {
    position: absolute; top: 211px;
    width: 511px; height: 291px;
    border-radius: 22px; overflow: hidden;
    background: var(--card-white);
  }
  .card--front { left: 78px; }
  .card--back { left: 609px; }
  .card svg.layer { position: absolute; inset: 0; }

  .brand { position: absolute; display: flex; align-items: center; }
  .brand__square { background: var(--ink); flex: none; }
  .brand__name {
    color: var(--ink); font-weight: 800; line-height: 0.95;
    text-transform: uppercase; letter-spacing: 0.5px;
  }
  .card--front .brand { left: 42px; top: 100px; gap: 16px; }
  .card--front .brand__square { width: 92px; height: 92px; }
  .card--front .brand__name { font-size: 40px; }
  .card--back .brand { left: 26px; top: 23px; gap: 12px; }
  .card--back .brand__square { width: 72px; height: 72px; }
  .card--back .brand__name { font-size: 31px; }

  .person { position: absolute; left: 25px; top: 131px; color: var(--ink); font-size: 13.5px; line-height: 16px; }
  .person__name { color: var(--safety-yellow); font-size: 17px; line-height: 20px; }

  .contact { position: absolute; right: 16px; top: 157px; text-align: right; color: var(--text-light); font-size: 13.5px; line-height: 16.2px; }
  .contact__row { display: flex; justify-content: flex-end; align-items: center; gap: 8px; }
  .contact__icon { width: 14px; height: 14px; flex: none; color: var(--safety-yellow); font-size: 11px; text-align: center; line-height: 14px; }
  .contact__address { color: var(--safety-yellow); margin-top: 4px; line-height: 17px; }
</style>
</head>
<body>

<section class="card card--front" aria-label="Business card front">
  <svg class="layer" width="511" height="291" viewBox="0 0 511 291">
    <rect class="tape" x="0" y="0" width="511" height="42" fill="var(--safety-yellow)" role="img" aria-label="Caution tape stripe pattern"/>
    <rect x="0" y="42" width="511" height="14" fill="var(--ink)"/>
    <rect x="0" y="56" width="511" height="8" fill="var(--grime)"/>
    <rect x="0" y="226" width="511" height="8" fill="var(--grime)"/>
    <rect x="0" y="234" width="511" height="14" fill="var(--ink)"/>
    <rect class="tape" x="0" y="248" width="511" height="43" fill="var(--safety-yellow)" role="img" aria-label="Caution tape stripe pattern"/>
  </svg>
  <div class="brand">
    <span class="brand__square"></span>
    <span class="brand__name">Halvorsen<br>Construction</span>
  </div>
</section>

<section class="card card--back" aria-label="Business card back">
  <svg class="layer" width="511" height="291" viewBox="0 0 511 291">
    <path d="M62 291 C140 210 240 160 340 150 C250 170 160 220 95 291 Z" fill="var(--swoosh-light)"/>
    <path d="M100 291 C170 220 260 170 350 150 C265 175 185 225 125 291 Z" fill="var(--safety-yellow)"/>
    <path d="M130 291 C200 215 290 160 360 149 C420 141 470 138 511 138 L511 291 Z" fill="var(--panel-dark)"/>
  </svg>

  <div class="brand">
    <span class="brand__square"></span>
    <span class="brand__name">Halvorsen<br>Construction</span>
  </div>

  <div class="person">
    <p class="person__name">Dale Halvorsen</p>
    <p>Owner</p>
    <p>General Contractor</p>
  </div>

  <div class="contact">
    <p class="contact__row">555-555-0147
      <svg class="contact__icon" viewBox="0 0 14 14" aria-label="Office"><path d="M1 5 C3 2 11 2 13 5 L11 6 L10 4.5 L4 4.5 L3 6 Z M3 7 L11 7 L12 12 L2 12 Z" fill="currentColor"/></svg></p>
    <p class="contact__row">555-555-0148 <span class="contact__icon">Fx</span></p>
    <p class="contact__row">555-555-0193
      <svg class="contact__icon" viewBox="0 0 14 14" aria-label="Cell"><rect x="4" y="1.5" width="6" height="11" rx="1" fill="none" stroke="currentColor" stroke-width="1.2"/></svg></p>
    <p class="contact__row">halvorsenconstruction@qvl-mail.net
      <svg class="contact__icon" viewBox="0 0 14 14" aria-label="Email"><rect x="2" y="3.5" width="10" height="7" fill="currentColor"/><path d="M2 3.5 L7 7.5 L12 3.5" fill="none" stroke="var(--panel-dark)" stroke-width="1"/></svg></p>
    <p class="contact__row">halvorsenconstruction-example.com
      <svg class="contact__icon" viewBox="0 0 14 14" aria-label="Website"><g fill="none" stroke="currentColor" stroke-width="1"><circle cx="7" cy="7" r="5"/><ellipse cx="7" cy="7" rx="2.2" ry="5"/><path d="M2 7 H12"/></g></svg></p>
    <p class="contact__address">482 Commerce Ridge Road<br>Brookfield Bend, Vermont 35871</p>
  </div>
</section>

</body>
</html>
```